Looking for updated Letterhead and Compliments Slips to go with our new updated logo. This stationary will be used for letters to suppliers and customers so needs to be practical while also quite classic.

We are an engineering company so needs to be clean and precise

Target Market(s)

SME'S and large automotive customers

Industry/Entity Type

Automotive

Font styles to use
Sans Serif

Colors
85acd3
0356a4
0792cd
33a6d7
85abd2
ffffff

Requirements
Must have
• Address details as below
• KT Fabrications Limited
• Marbury Close
• Brackenford
• Elmshire
• DN47 3XP, UK
• Telephone: +44 (0)1632 960418
• Fax: +44 (0)1632 960735
• Email: sales@ktfabrications.example
• Web: www.ktfabrications.example
Nice to have
• Nice to have some element of being a British Manufacturer

```html
<!DOCTYPE html>
<html lang="en">
<head>
<meta charset="utf-8">
<title>KT Fabrications – Letterhead and Compliments Slip</title>
<link rel="stylesheet" href="https://fonts.googleapis.com/css2?family=Open+Sans:wght@400;600&family=Roboto:wght@400;500;700&family=Great+Vibes&display=swap">
<style>
  :root {
    --backdrop: #464646;
    --paper: #f5f4f2;
    --brand-blue: #0356a4;
    --brand-navy: #0a4c94;
    --ink: #3c3c3c;
    --ink-soft: #555555;
    --rule: #d6d6d6;
    --band-dark: #1a1a1a;
    --white: #ffffff;
  }
  * { box-sizing: border-box; margin: 0; padding: 0; }
  html, body { width: 1200px; height: 893px; overflow: hidden; }
  body { background: var(--backdrop); position: relative; font-family: "Open Sans", sans-serif; color: var(--ink); }

  .sheet { position: absolute; background: var(--paper); box-shadow: 0 2px 6px rgba(0,0,0,.35); overflow: hidden; }

  /* Letterhead */
  .letterhead { left: 70px; top: 38px; width: 576px; height: 813px; }
  .wordmark { font-family: "Roboto", sans-serif; font-weight: 500; color: var(--brand-blue); letter-spacing: 3.2px; white-space: nowrap; display: flex; align-items: center; gap: 7px; }
  .wordmark .dot { width: 9px; height: 9px; border-radius: 50%; background: var(--brand-blue); flex: none; }
  .letterhead .wordmark { position: absolute; top: 97px; left: 0; width: 100%; justify-content: center; font-size: 13px; }
  .letterhead .header-rule { position: absolute; top: 121px; left: 57px; width: 474px; height: 1px; background: linear-gradient(to right, transparent, var(--rule) 15%, var(--rule) 85%, transparent); }
  .letterhead .address { position: absolute; top: 128px; left: 0; width: 100%; text-align: center; font-family: "Roboto", sans-serif; font-size: 9.6px; line-height: 14px; color: var(--ink-soft); }
  .letterhead .address strong { font-weight: 700; color: var(--ink); }
  .contact-line { display: inline-flex; align-items: center; gap: 3px; }
  .contact-line svg { width: 9px; height: 9px; fill: var(--brand-blue); flex: none; }
  .contact-line + .contact-line { margin-left: 4px; }

  .letter-body { position: absolute; left: 60px; top: 226px; width: 466px; }
  .letter-body p { font-size: 8.5px; line-height: 13.9px; color: var(--ink-soft); margin-bottom: 13.9px; text-align: justify; }
  .letter-body .salutation { font-size: 14.5px; line-height: 20px; color: var(--ink); margin-bottom: 23px; text-align: left; }
  .letter-body .sign-off { font-size: 8.5px; color: var(--ink-soft); margin-top: 24px; margin-bottom: 0; }
  .signature { display: block; width: 76px; height: 30px; margin: 10px 0 6px; background: linear-gradient(90deg, rgba(40,40,40,.15), rgba(40,40,40,.05)); border-radius: 2px; }
  .signatory { font-size: 9.5px; line-height: 15px; color: var(--ink-soft); padding-left: 3px; }

  .footer-band { position: absolute; left: 0; width: 100%; height: 20px; display: flex; }
  .footer-band .band-blue { background: var(--brand-navy); height: 100%; position: relative; }
  .footer-band .band-dark { background: var(--band-dark); flex: 1; height: 100%; }
  .footer-band .site { position: absolute; top: 0; line-height: 20px; font-family: "Roboto", sans-serif; font-size: 9.5px; letter-spacing: 1.9px; color: var(--white); }
  .footer-band .marker { position: absolute; top: 3px; width: 14px; height: 14px; border-radius: 50%; border: 2px solid var(--white); background: var(--brand-navy); }
  .letterhead .footer-band { top: 783px; }
  .letterhead .band-blue { width: 466px; }
  .letterhead .site { left: 58px; }
  .letterhead .marker { left: 459px; }

  /* Compliments slip */
  .comp-slip { left: 463px; top: 473px; width: 650px; height: 295px; }
  .comp-slip .wordmark { position: absolute; top: 82px; left: 36px; font-size: 13px; }
  .comp-slip .divider { position: absolute; left: 473px; top: 25px; width: 1px; height: 80px; background: var(--rule); }
  .comp-slip .address { position: absolute; left: 490px; top: 25px; font-family: "Roboto", sans-serif; font-size: 9.6px; line-height: 12px; color: var(--ink-soft); }
  .comp-slip .address .contact-line { display: flex; margin: 0; line-height: 13.6px; }
  .comp-slip .address .first-contact { margin-top: 5px; }
  .compliments { position: absolute; left: 165px; top: 158px; font-family: "Great Vibes", cursive; font-size: 54px; color: var(--brand-navy); white-space: nowrap; }
  .comp-slip .footer-band { top: 265px; }
  .comp-slip .band-blue { width: 540px; }
  .comp-slip .site { left: 34px; }
  .comp-slip .marker { left: 533px; }
</style>
</head>
<body>

<svg width="0" height="0" style="position:absolute">
  <symbol id="icon-phone" viewBox="0 0 10 10"><path d="M2.1 0.6l1.5 1.9-0.8 1.1c0.6 1.3 1.5 2.2 2.7 2.8l1.1-0.8 1.9 1.5-0.9 1.6C4.8 8.6 1.3 5.2 0.6 1.5z"/></symbol>
  <symbol id="icon-fax" viewBox="0 0 10 10"><path d="M2.5 1h5v2h-5zM0.5 3.5h9v4h-1.5v-1.5h-6v1.5h-1.5zM2.5 6.5h5v2.5h-5z"/></symbol>
  <symbol id="icon-mail" viewBox="0 0 10 10"><path d="M0.5 2h9v6h-9zM1.3 2.8v0.4l3.7 2.4 3.7-2.4v-0.4z" fill-rule="evenodd"/></symbol>
</svg>

<section class="sheet letterhead" aria-label="Letterhead">
  <div class="wordmark"><span class="dot"></span>KT FABRICATIONS</div>
  <div class="header-rule"></div>
  <div class="address">
    <div><strong>KT Fabrications Limited,</strong> Marbury Close, Brackenford, Elmshire, DN47 3XP, UK</div>
    <div>
      <span class="contact-line"><svg><use href="#icon-phone"/></svg>+44 (0)1632 960418</span>
      <span class="contact-line"><svg><use href="#icon-fax"/></svg>+44 (0)1632 960735</span>
      <span class="contact-line"><svg><use href="#icon-mail"/></svg>sales@ktfabrications.example</span>
    </div>
  </div>

  <div class="letter-body">
    <p class="salutation">Dear Mr. Ellison,</p>
    <p>Lorem ipsum dolor sit amet, consectetur adipiscing elit. Donec orci purus, luctus vitae dignissim eu, iaculis sed purus. Vivamus faucibus, ipsum nec aliquet viverra, leo mauris condimentum ligula, sit amet sagittis enim ligula quis arcu. Nam egestas tortor id nisi porttitor mattis. In tortor ante, ultricies in suscipit a, tempus non massa. Vivamus et auctor mi. Fusce vel massa nulla. Phasellus nec eros mauris, et scelerisque orci.</p>
    <p>Donec malesuada orci vitae nulla accumsan porta a id massa. Quisque accumsan iaculis magna sit amet fringilla. Maecenas consequat, magna eget tincidunt semper, odio nibh rutrum mi, id feugiat ante nisi eu risus. Vestibulum nunc orci, rhoncus a placerat in, ultricies in mi. Cras mattis varius eros, vel fringilla nisi suscipit eget. Quisque scelerisque sagittis nulla at porttitor.</p>
    <p>Sed id augue vitae urna euismod commodo aliquet a quam. Pellentesque arcu velit, cursus et malesuada ut, consequat et diam. Nullam erat sem, rhoncus id ullamcorper vitae, rhoncus et arcu. In ultricies ultricies nulla, ut rutrum nisi iaculis at. Donec eu magna a metus ornare faucibus. Fusce aliquet faucibus ultricies. Nulla gravida, sem arcu adipiscing lacus, ac bibendum nulla leo eu purus. Quisque nec diam san quis quis nibh. Vestibulum id purus lorem.</p>
    <p>It is a long established fact that a reader will be distracted by the readable content of a page when looking at its layout. The point of using Lorem Ipsum is that it has a more-or-less normal distribution of letters, as opposed to 'Content here, content here', making it look like readable English. Many desktop publishing packages use it.</p>
    <p class="sign-off">Sincerely,</p>
    <span class="signature" role="img" aria-label="Handwritten signature"></span>
    <div class="signatory">Daniel Rowe<br>CEO/ Founder</div>
  </div>

  <div class="footer-band">
    <div class="band-blue"><span class="site">www.ktfabrications.example</span><span class="marker"></span></div>
    <div class="band-dark"></div>
  </div>
</section>

<section class="sheet comp-slip" aria-label="Compliments slip">
  <div class="wordmark"><span class="dot"></span>KT FABRICATIONS</div>
  <div class="divider"></div>
  <div class="address">
    <div>KT Fabrications Limited</div>
    <div>Marbury Close, Brackenford</div>
    <div>Elmshire, DN47 3XP, UK</div>
    <span class="contact-line first-contact"><svg><use href="#icon-phone"/></svg>+44 (0)1632 960418</span>
    <span class="contact-line"><svg><use href="#icon-fax"/></svg>+44 (0)1632 960735</span>
    <span class="contact-line"><svg><use href="#icon-mail"/></svg>sales@ktfabrications.example</span>
  </div>
  <div class="compliments">With Compliments</div>
  <div class="footer-band">
    <div class="band-blue"><span class="site">www.ktfabrications.example</span><span class="marker"></span></div>
    <div class="band-dark"></div>
  </div>
</section>

</body>
</html>
```